Postcard Design

R.K Landscaping 484-883-7758Mulching Mowing Planting Spring and Fall Clean up

The colors I would like to work with Are black and green.I do have a Facebook page it's https://www.example-social.test/RK-Landscaping-904417362018834/

For my business logo I would like to put that either on the corner or in the background

Services: mowing, mulching, fall and spring cleanup, hedge trimming

Industry/Entity Type

Landscaping

Requirements
Must have
• Please use these pics
• I like Design #9926064
• and room for addresses to
Should not have
• the pics in the back of card

```html
<!DOCTYPE html>
<html lang="en">
<head>
<meta charset="utf-8">
<title>R.K Landscaping Postcard</title>
<link rel="stylesheet" href="https://fonts.googleapis.com/css2?family=Oswald:wght@500;700&family=Cabin:wght@700&family=Josefin+Sans:wght@300&display=swap">
<style>
  :root {
    --bg: #d8cdb8;
    --card-black: #0a0a0a;
    --leaf-green: #8dc63f;
    --wood-dark: #3a2e24;
    --wood-mid: #5c4a3a;
    --bamboo: #6b7a3a;
  }
  * { margin: 0; padding: 0; box-sizing: border-box; }
  html, body {
    width: 1200px; height: 801px; overflow: hidden;
    background: var(--bg);
  }
  .canvas {
    width: 1200px; height: 801px;
    display: flex; align-items: center; justify-content: center; gap: 48px;
  }
  .postcard {
    position: relative;
    width: 540px; height: 360px;
    overflow: hidden;
    box-shadow: 0 4px 14px rgba(0,0,0,0.25);
  }

  /* Front side */
  .postcard--front { background: var(--wood-dark); }
  .front-photo {
    position: absolute; inset: 0;
    background: linear-gradient(100deg, var(--wood-mid) 0%, var(--wood-dark) 45%, rgba(58,46,36,0.9) 60%, var(--bamboo) 100%);
  }
  .brand {
    position: absolute; left: 230px; top: 120px; width: 240px;
    text-align: center; color: var(--leaf-green);
    font-family: "Oswald", sans-serif; font-weight: 500;
  }
  .brand-name {
    display: inline-flex; align-items: center; gap: 8px;
    font-size: 22px; line-height: 1.1; white-space: nowrap;
  }
  .brand-dot {
    width: 14px; height: 14px; border-radius: 50%;
    background: var(--leaf-green); flex: none;
  }
  .brand-phone {
    font-size: 18px; margin-top: 10px; letter-spacing: 0.5px;
  }
  .service-strip {
    position: absolute; left: 0; right: 0; bottom: 46px;
    text-align: center; color: var(--leaf-green);
    font-family: "Oswald", sans-serif; font-weight: 500;
    font-size: 12.5px; letter-spacing: 0.6px; text-transform: uppercase;
    white-space: nowrap;
  }

  /* Back side */
  .postcard--back { background: var(--card-black); }
  .corner-brand {
    position: absolute; right: 30px; top: 22px; width: 140px;
    text-align: center; color: var(--leaf-green);
    font-family: "Oswald", sans-serif; font-weight: 500;
  }
  .corner-brand .brand-name { font-size: 14px; gap: 6px; }
  .corner-brand .brand-dot { width: 9px; height: 9px; }
  .corner-brand .brand-phone { font-size: 11px; margin-top: 5px; }

  .service-list {
    position: absolute; left: 30px; top: 150px;
    color: var(--leaf-green); text-transform: uppercase; line-height: 1;
    font-weight: normal;
  }
  .service-list .line { display: block; white-space: nowrap; }
  .service-list .mowing {
    font-family: "Cabin", sans-serif; font-weight: 700; font-size: 50px;
  }
  .service-list .mulching {
    font-family: "Josefin Sans", sans-serif; font-weight: 300; font-size: 46px; margin-top: 2px;
  }
  .service-list .cleanup {
    font-family: "Oswald", sans-serif; font-weight: 700; font-size: 40px; margin-top: 2px;
  }
  .service-list .hedge {
    font-family: "Josefin Sans", sans-serif; font-weight: 300; font-size: 38px; margin-top: 4px; letter-spacing: 1px;
  }
</style>
</head>
<body>
<main class="canvas">
  <section class="postcard postcard--front">
    <div class="front-photo" role="img" aria-label="Photo of a wooden fence with bamboo stalks and leaves"></div>
    <div class="brand">
      <div class="brand-name"><span class="brand-dot"></span>R.K Landscaping</div>
      <div class="brand-phone">555-216-0493</div>
    </div>
    <p class="service-strip">Mowing, mulching, fall and spring cleanup, hedge trimming</p>
  </section>

  <section class="postcard postcard--back">
    <div class="corner-brand">
      <div class="brand-name"><span class="brand-dot"></span>R.K Landscaping</div>
      <div class="brand-phone">555-216-0493</div>
    </div>
    <h2 class="service-list">
      <span class="line mowing">Mowing,</span>
      <span class="line mulching">Mulching,</span>
      <span class="line cleanup">Fall &amp; Spring Cleanup,</span>
      <span class="line hedge">Hedge Trimming</span>
    </h2>
  </section>
</main>
</body>
</html>
```